Movie Poster/DVD jacket for Short Documentary

I am a documentary filmmaker who just completed a project titled "Sister Marigold". Here is the logline (short description of the movie): "An Oklahoma family is ripped apart after their 15-year-old son brutally murders his older sister in 1974. Controversy swirls around the case after his parents decide to hire a prominent defense attorney to keep him out of jail." I have several good photos of the family involved. I am in the process of submitting the film to several festivals and I want a professional looking movie poster that can be sent with film submissions. The look needs to dramatic and serious.
Updates

Project Deadline Extended Reason: We just had several more submission enter today and need a few more days to evaluate. Thank you for you patience. Added Thursday, November 19, 2015

Target Market(s)

Film festivals, television

Industry/Entity Type

Movie

Colors
f04a50

Requirements
Must have
• the color red and have a similar appearance to the sample movie posters.
• Also, tagline: turning a blind eye into broken hearts
• Directors name: a film by Rob Haskett
Nice to have
• rough
Should not have
• Not a gruesome look.

```html
<!DOCTYPE html>
<html lang="en">
<head>
<meta charset="utf-8">
<title>Sister Marigold — a film by Rob Haskett</title>
<link rel="stylesheet" href="https://fonts.googleapis.com/css2?family=Bodoni+Moda:wght@500;700&family=IM+Fell+English:ital@0;1&family=Old+Standard+TT:wght@400;700&display=swap">
<style>
  :root {
    --wall-light: #b9c0a8;
    --wall-mid: #8e9a7e;
    --wall-dark: #5f6b55;
    --paper: #ecebe4;
    --paper-shade: #d8d6cc;
    --ink: #1d1a17;
    --ink-soft: #3a342e;
    --sepia-light: #b8a789;
    --sepia-dark: #4a3e30;
    --photo-border: #e8e0cf;
    --red: #f04a50;
    --red-deep: #c8202a;
  }
  * { margin: 0; padding: 0; box-sizing: border-box; }
  html, body { width: 900px; height: 1200px; overflow: hidden; background: var(--wall-mid); }
  .poster {
    position: relative;
    width: 900px;
    height: 1200px;
    overflow: hidden;
  }
  .wallpaper {
    position: absolute; inset: 0;
    background:
      radial-gradient(ellipse at 50% 40%, var(--wall-light) 0%, var(--wall-mid) 60%, var(--wall-dark) 100%);
  }
  .clipping {
    position: absolute;
    background: var(--paper);
    box-shadow: 0 6px 14px rgba(0,0,0,0.35);
    padding: 18px 22px;
    color: var(--ink);
    font-family: "Old Standard TT", serif;
  }
  .clipping--left { left: 60px; top: -20px; width: 370px; height: 290px; transform: rotate(-4deg); }
  .clipping--right { left: 530px; top: -24px; width: 340px; height: 250px; transform: rotate(3deg); }
  .clipping__headline {
    font-weight: 700;
    font-size: 40px;
    line-height: 1.02;
    margin-top: 24px;
  }
  .clipping--right .clipping__headline { font-size: 30px; margin-top: 30px; }
  .clipping__body {
    margin-top: 12px;
    font-size: 13px;
    line-height: 1.35;
    color: var(--ink-soft);
    columns: 2;
    column-gap: 14px;
  }
  .splatter {
    position: absolute;
    border-radius: 50%;
    background: radial-gradient(circle, var(--red-deep) 0%, rgba(200,32,42,0.55) 45%, rgba(200,32,42,0) 72%);
  }
  .splatter--left { left: -70px; top: 330px; width: 260px; height: 200px; }
  .splatter--bottom { left: 20px; top: 1020px; width: 360px; height: 230px; }
  .family-photo {
    position: absolute;
    left: 228px; top: 140px;
    width: 560px; height: 540px;
    background: var(--photo-border);
    padding: 22px;
    transform: rotate(-2deg);
    box-shadow: 0 10px 24px rgba(0,0,0,0.45);
  }
  .family-photo__image {
    width: 100%; height: 100%;
    background: linear-gradient(160deg, var(--sepia-light) 0%, #8d7c62 45%, var(--sepia-dark) 100%);
  }
  .title {
    position: absolute;
    left: 0; right: 0; top: 690px;
    text-align: center;
    font-family: "Bodoni Moda", serif;
    font-weight: 700;
    font-size: 108px;
    line-height: 0.9;
    letter-spacing: 4px;
    color: var(--ink);
    text-transform: uppercase;
  }
  .tagline {
    position: absolute;
    left: 0; right: 0; top: 882px;
    text-align: center;
    font-family: "IM Fell English", serif;
    font-style: italic;
    font-size: 40px;
    color: var(--ink);
  }
  .credit-intro {
    position: absolute;
    left: 0; right: 0; top: 928px;
    text-align: center;
    font-family: "IM Fell English", serif;
    font-style: italic;
    font-size: 36px;
    color: var(--ink);
  }
  .director {
    position: absolute;
    left: 0; right: 0; top: 968px;
    text-align: center;
    font-family: "Bodoni Moda", serif;
    font-weight: 700;
    font-size: 62px;
    letter-spacing: 3px;
    color: var(--red-deep);
    text-transform: uppercase;
  }
</style>
</head>
<body>
  <main class="poster">
    <div class="wallpaper" role="img" aria-label="Faded green damask wallpaper background"></div>

    <article class="clipping clipping--left">
      <h2 class="clipping__headline">Teen held in killing of sister</h2>
      <p class="clipping__body">A local boy, 15, was taken into custody Tuesday after his older sister was found dead in the family home. Police said the case remains under review by county officials.</p>
    </article>

    <article class="clipping clipping--right">
      <h2 class="clipping__headline">Not as Adult — Plea for Teen-Age Boy</h2>
      <p class="clipping__body">Defense counsel asked the court to hear the case in juvenile session, citing age and family support.</p>
    </article>

    <div class="splatter splatter--left" role="img" aria-label="Red paint splatter"></div>
    <div class="splatter splatter--bottom" role="img" aria-label="Red paint splatter"></div>

    <figure class="family-photo">
      <div class="family-photo__image" role="img" aria-label="Vintage sepia family photograph of a sister and her younger brother"></div>
    </figure>

    <h1 class="title">Sister<br>Marigold</h1>
    <p class="tagline">Turning a blind eye into broken hearts</p>
    <p class="credit-intro">a film by</p>
    <p class="director">Rob Haskett</p>
  </main>
</body>
</html>
```